Specialised investor in e-mobility and energy wants business card design

We need a business card design that fits our existing corporate design. <The look and feel must be 'sharp'/'clean', dynamic, communicate momentum, professionalism etc (as one would imagine from a firm in the financial sector). We like the idea of a reverse-side of the card that includes the logo, and the name and contact details on the other. We expect the deliverable to be whatever format might be required to be able to get cards printed directly by a service such as tandor press. Our website is www.orm.capital

```html
<!DOCTYPE html>
<html lang="en">
<head>
<meta charset="utf-8">
<title>ORM Capital — Business Card</title>
<link href="https://fonts.googleapis.com/css2?family=Montserrat:wght@400;500;700&display=swap" rel="stylesheet">
<style>
  :root {
    --page-bg: #e9e6e0;
    --card-white: #ffffff;
    --green-dark: #2e4d23;
    --green-light: #8ab54a;
    --ink: #2b2b2b;
    --logo-on-dark: #b8c6a6;
  }
  * { margin: 0; padding: 0; box-sizing: border-box; }
  html, body { width: 900px; height: 1200px; overflow: hidden; }
  body {
    background: var(--page-bg);
    font-family: "Montserrat", Arial, sans-serif;
    position: relative;
  }
  .card {
    position: absolute;
    left: 80px;
    width: 742px;
    height: 440px;
    border-radius: 28px;
    overflow: hidden;
    box-shadow: 0 4px 10px rgba(0,0,0,0.25);
  }
  .card-front { top: 132px; background: var(--card-white); }
  .card-back { top: 638px; background: var(--green-dark); }

  .footer-band {
    position: absolute;
    left: 0;
    right: 0;
    bottom: 0;
    height: 46px;
    background: var(--green-dark);
  }
  .footer-rule {
    position: absolute;
    left: 0;
    right: 0;
    bottom: 54px;
    height: 6px;
    background: var(--green-light);
  }

  .brand-front {
    position: absolute;
    left: 25px;
    top: 222px;
    font-size: 44px;
    font-weight: 500;
    color: var(--green-dark);
    letter-spacing: 0.5px;
    white-space: nowrap;
  }

  .divider {
    position: absolute;
    left: 406px;
    top: 140px;
    width: 2px;
    height: 188px;
    background: var(--green-light);
  }

  .contact-block {
    position: absolute;
    left: 461px;
    top: 136px;
    color: var(--ink);
  }
  .person-name {
    font-size: 26px;
    font-weight: 700;
    color: var(--green-dark);
    line-height: 32px;
  }
  .person-role { font-size: 15px; line-height: 20px; margin-bottom: 18px; }
  .contact-list { list-style: none; }
  .contact-list li {
    display: flex;
    align-items: center;
    font-size: 16px;
    line-height: 22px;
  }
  .contact-icon { width: 12px; height: 12px; margin: 0 12px 0 2px; flex: none; }
  .address { margin-top: 14px; font-size: 16px; line-height: 20px; }

  .brand-back {
    position: absolute;
    left: 0;
    right: 0;
    top: 170px;
    text-align: center;
    font-size: 78px;
    font-weight: 500;
    color: var(--logo-on-dark);
    letter-spacing: 1px;
  }
</style>
</head>
<body>

<section class="card card-front" aria-label="Card front">
  <div class="footer-rule"></div>
  <div class="footer-band"></div>

  <div class="brand-front">ORM Capital</div>
  <div class="divider"></div>

  <div class="contact-block">
    <h1 class="person-name">Daniel Hartwell</h1>
    <p class="person-role">Owner</p>
    <ul class="contact-list">
      <li>
        <svg class="contact-icon" viewBox="0 0 12 12" aria-hidden="true">
          <path d="M1 4 Q6 0 11 4 L9 5 L8 3.5 L4 3.5 L3 5 Z M2.5 6 L9.5 6 L10.5 11 L1.5 11 Z" fill="var(--green-light)"/>
        </svg>
        +41 79555 0148
      </li>
      <li>
        <svg class="contact-icon" viewBox="0 0 12 12" aria-hidden="true">
          <rect x="0.5" y="2.5" width="11" height="7.5" fill="var(--green-light)"/>
          <path d="M0.5 2.5 L6 7 L11.5 2.5" fill="none" stroke="#fff" stroke-width="1"/>
        </svg>
        daniel@orm.capital
      </li>
      <li>
        <svg class="contact-icon" viewBox="0 0 12 12" aria-hidden="true">
          <circle cx="6" cy="6" r="5.5" fill="var(--green-light)"/>
          <path d="M3 3.5 Q5 4 4.5 6 Q6.5 7 6 9.5 M8 2.5 Q7.5 4.5 9.5 5" fill="none" stroke="#fff" stroke-width="1"/>
        </svg>
        www.orm.capital
      </li>
    </ul>
    <p class="address">27 Meridian Way, Suite 204<br>Halston, PA 18820</p>
  </div>
</section>

<section class="card card-back" aria-label="Card back">
  <div class="brand-back">ORM Capital</div>
</section>

</body>
</html>
```